Create a Professional PowerPoint Slide Deck

I need a professional looking and editable PowerPoint presentation with contents based on the attached PDF.

I would like to see the following;
- add design elements to every slide (cover, title, contents etc)
- enhance the graphs or charts
- same copy will be used
I'm attaching the document to be put into powerpoint (KWRO white paper: "Cargo Wise")

Target Market(s)

Executives and managers responsible for the distribution of products

Industry/Entity Type

It Professional

Font styles to use
Serif

Colors

Designer to choose colors to be used in the design.

Requirements
Must have
• The format should be portrait orientation as this may be printed on paper and converted to PDF for distribution
• Complete conversion of all pages in the attached White Paper
• Upgraded graphics and formatting
Nice to have
• Any creative ideas to make the presentation more attractive or easier to understand
• Color scheme should complement the KWRO Freightlines Logo (red and black)

```html
<!DOCTYPE html>
<html lang="en">
<head>
<meta charset="utf-8">
<title>A Better Way to Handle Multiple Quotes</title>
<link rel="stylesheet" href="https://fonts.googleapis.com/css2?family=Open+Sans:wght@400&family=Tinos:wght@400;700&display=swap">
<style>
  :root {
    --page: #ffffff;
    --ink: #1e1e1e;
    --heading: #222222;
    --sky-top: #5a8fc4;
    --sky-mid: #a9c7e2;
    --sun: #f4efe2;
    --dock: #6b5e5a;
    --crane: #9c3a3c;
    --node-blue: #1e7fc2;
    --node-green: #2aa34a;
    --box-blue: #3d8fd1;
    --box-edge: #2468a8;
    --shipper-text: #f2d84b;
    --line-blue: #2f7dc0;
    --label: #4a4a4a;
  }
  html, body {
    margin: 0;
    padding: 0;
    width: 831px;
    height: 1200px;
    overflow: hidden;
    background: var(--page);
  }
  .page {
    position: relative;
    width: 831px;
    height: 1200px;
    background: var(--page);
    color: var(--ink);
    font-family: "Open Sans", Arial, sans-serif;
  }
  .hero-photo {
    position: absolute;
    left: 0; top: 0;
    width: 831px; height: 258px;
    background:
      linear-gradient(180deg, transparent 0%, transparent 72%, var(--dock) 78%, #3e3a3a 100%),
      radial-gradient(circle at 88% 42%, var(--sun) 0%, rgba(244,239,226,0.6) 14%, transparent 38%),
      linear-gradient(180deg, var(--sky-top) 0%, var(--sky-mid) 55%, #d9dfe2 72%);
  }
  .section-title {
    position: absolute;
    left: 38px;
    width: 760px;
    margin: 0;
    font-family: "Tinos", "Times New Roman", serif;
    font-weight: 700;
    color: var(--heading);
    letter-spacing: -0.3px;
  }
  .title-main { top: 268px; font-size: 27px; line-height: 31px; }
  .title-sub  { top: 908px; font-size: 27px; line-height: 31px; }
  .body-copy {
    position: absolute;
    left: 38px;
    width: 736px;
    margin: 0;
    font-size: 15.4px;
    line-height: 21.6px;
  }
  .copy-tms { top: 344px; }
  .copy-3pl { top: 952px; }
  .flow-diagram {
    position: absolute;
    left: 290px;
    top: 643px;
  }
  .figure-caption {
    position: absolute;
    left: 38px;
    top: 858px;
    width: 760px;
    margin: 0;
    font-family: "Tinos", "Times New Roman", serif;
    font-size: 16.4px;
    line-height: 21px;
  }
</style>
</head>
<body>
<main class="page">
  <div class="hero-photo" role="img" aria-label="Container port with red gantry cranes against a bright blue sky and low sun"></div>

  <h1 class="section-title title-main">A Better Way to Handle Multiple Quotes – use a TMS (Transportation Management System)</h1>

  <p class="body-copy copy-tms">Is there a way to get multiple quotes without spending so much time and effort asking for quotes, reviewing them and then awarding the business? In a word, yes. If you use a Transportation Management System (TMS) you can enter the shipment information on your shipment once and get immediate quotes from multiple carriers (Fig. 2). You can select the carrier you want and get your shipment underway in about a minute. In addition to saving time and reducing stress, the TMS will permit you to print the BOL and Labels so your shipment is ready for the driver to pick up. You access the TMS via the web, so there is no special equipment to purchase. You will need accounts with each carrier and you should negotiate your own rates with them. The TMS will typically permit you to track shipments on all carriers, and it can also capture the quote information for reference later. Perhaps the most commonly overlooked, the data from all of your shipments is captured and retained in the TMS, so you can produce reports at the end of the month or on demand.</p>

  <svg class="flow-diagram" width="250" height="206" viewBox="0 0 250 206" aria-label="Shipper connected to a TMS that queries multiple carriers">
    <defs>
      <marker id="arrow-head" markerWidth="6" markerHeight="6" refX="5" refY="3" orient="auto-start-reverse">
        <path d="M0,0 L6,3 L0,6 z" fill="var(--line-blue)"/>
      </marker>
    </defs>
    <g font-family="Open Sans, Arial, sans-serif" font-size="9" fill="var(--label)">
      <text x="130" y="12">Queries/Quotes</text>
      <text x="62" y="61">Quotes/</text>
      <text x="62" y="73">Booking</text>
      <text x="64" y="147">Historical</text>
      <text x="74" y="159">Data</text>
    </g>
    <rect x="0" y="84" width="59" height="49" fill="var(--box-blue)" stroke="var(--box-edge)"/>
    <text x="29.5" y="112" text-anchor="middle" font-family="Open Sans, Arial, sans-serif" font-size="10" font-style="italic" font-weight="700" fill="var(--shipper-text)">Shipper</text>
    <rect x="107" y="91" width="33" height="32" fill="var(--box-blue)" stroke="var(--box-edge)"/>
    <text x="123.5" y="111" text-anchor="middle" font-family="Open Sans, Arial, sans-serif" font-size="9" font-style="italic" font-weight="700" fill="#ffffff">TMS</text>
    <g stroke="var(--line-blue)" stroke-width="1.2">
      <line x1="62" y1="101" x2="104" y2="101" marker-start="url(#arrow-head)" marker-end="url(#arrow-head)"/>
      <line x1="62" y1="114" x2="104" y2="114" marker-start="url(#arrow-head)" marker-end="url(#arrow-head)"/>
    </g>
    <g stroke="var(--line-blue)" stroke-width="1.2" marker-start="url(#arrow-head)" marker-end="url(#arrow-head)">
      <line x1="143" y1="100" x2="215" y2="22"/>
      <line x1="143" y1="102" x2="215" y2="44"/>
      <line x1="143" y1="104" x2="215" y2="66"/>
      <line x1="143" y1="106" x2="215" y2="88"/>
      <line x1="143" y1="107" x2="215" y2="109"/>
      <line x1="143" y1="109" x2="215" y2="130"/>
      <line x1="143" y1="111" x2="215" y2="152"/>
      <line x1="143" y1="113" x2="215" y2="174"/>
      <line x1="143" y1="115" x2="215" y2="195"/>
    </g>
    <g font-family="Open Sans, Arial, sans-serif" font-size="9" font-weight="700" font-style="italic" fill="#ffffff" text-anchor="middle">
      <circle cx="225" cy="20" r="8" fill="var(--node-blue)"/><text x="225" y="23">T</text>
      <circle cx="225" cy="42" r="8" fill="var(--node-green)"/><text x="225" y="45">T</text>
      <circle cx="225" cy="64" r="8" fill="var(--node-blue)"/><text x="225" y="67">T</text>
      <circle cx="225" cy="86" r="8" fill="var(--node-blue)"/><text x="225" y="89">T</text>
      <circle cx="225" cy="108" r="8" fill="var(--node-blue)"/><text x="225" y="111">T</text>
      <circle cx="225" cy="130" r="8" fill="var(--node-blue)"/><text x="225" y="133">T</text>
      <circle cx="225" cy="152" r="8" fill="var(--node-blue)"/><text x="225" y="155">T</text>
      <circle cx="225" cy="174" r="8" fill="var(--node-blue)"/><text x="225" y="177">T</text>
      <circle cx="225" cy="196" r="8" fill="var(--node-blue)"/><text x="225" y="199">T</text>
    </g>
  </svg>

  <p class="figure-caption">Figure 2. Using a TMS saves time by entering the quote request, receiving multiple quotes assigning the load and printing BOL and Shipping Labels in less than a minute</p>

  <h2 class="section-title title-sub">Beyond the TMS – Using a 3PL</h2>

  <p class="body-copy copy-3pl">TMS systems are commonly web based and very easy to use. They usually require a monthly fee depending on the number of users and monthly shipments. There may also be a fee for setting up your carriers in the system to get started. What else can you do to improve your logistics system? If you utilize the services of a 3PL, you will often be able to get a TMS system for no charge as long as you book with their carriers. The 3PL is bringing much more business to the negotiating table than you will alone, so their rates are likely to be lower than yours. So, you get lower rates, spend less time quoting and booking as well as all the other benefits of a TMS while saving money. You also get a single invoice each month covering all of your shipments.</p>
</main>
</body>
</html>
```